Industrial Professional Business Card Design (Vantrel Systems)

Would like professional looking business cards. Not too busy leaning towards minimal. Should have a slogan like:
"Industrial Automation and Control".

We are a tech company that programs industrial PLC computers. We also develop custom hardware solutions. Please use the logo for inspiration.

Target Market(s)

Mining, industrial, processing, automation, factory

Industry/Entity Type

Engineering

Contact Information for Business Card

Name, phone, email, website. job title.

Font styles to use
Other font styles liked:
• droid sans

Requirements
Must have
• Use colours that go well with the logo. Not too busy design.

```html
<!DOCTYPE html>
<html lang="en">
<head>
<meta charset="utf-8">
<title>Vantrel Systems – Business Card</title>
<link href="https://fonts.googleapis.com/css2?family=Noto+Sans:wght@400;600;700&display=swap" rel="stylesheet">
<style>
  :root {
    --page-bg: #e6e6e4;
    --card-dark: #161616;
    --card-light: #ffffff;
    --navy: #1d2f5a;
    --steel-blue: #3d6fa6;
    --orange: #ee6a24;
    --text-dark: #1d2a4a;
  }
  * { margin: 0; padding: 0; box-sizing: border-box; }
  html, body {
    width: 1200px;
    height: 825px;
    overflow: hidden;
    background: var(--page-bg);
    font-family: "Noto Sans", Arial, sans-serif;
  }
  .canvas {
    position: relative;
    width: 1200px;
    height: 825px;
  }
  .card {
    position: absolute;
    width: 525px;
    height: 300px;
    top: 262px;
    border-radius: 3px;
    box-shadow: 0 6px 18px rgba(0,0,0,0.18);
    overflow: hidden;
  }
  .card--front {
    left: 50px;
    background: var(--card-dark);
    display: flex;
    align-items: center;
    justify-content: center;
  }
  .card--back {
    left: 625px;
    background: var(--card-light);
  }
  .brand {
    display: flex;
    align-items: center;
    gap: 14px;
  }
  .brand__dot {
    width: 46px;
    height: 46px;
    border-radius: 50%;
    background: var(--orange);
  }
  .brand__name {
    font-size: 36px;
    font-weight: 400;
    color: var(--steel-blue);
    letter-spacing: 0.5px;
  }
  .card--back .brand {
    position: absolute;
    right: 28px;
    top: 64px;
    gap: 10px;
  }
  .card--back .brand__dot {
    width: 34px;
    height: 34px;
  }
  .card--back .brand__name {
    font-size: 19px;
    color: var(--navy);
  }
  .holder {
    position: absolute;
    left: 34px;
    top: 74px;
  }
  .holder__name {
    font-size: 25px;
    font-weight: 400;
    color: var(--text-dark);
    line-height: 1;
  }
  .divider {
    position: absolute;
    left: 0;
    right: 0;
    top: 112px;
    height: 2px;
    background: var(--orange);
  }
  .holder__title {
    position: absolute;
    left: 34px;
    top: 120px;
    font-size: 12px;
    font-weight: 700;
    letter-spacing: 1.5px;
    color: var(--orange);
  }
  .contacts {
    position: absolute;
    left: 34px;
    right: 28px;
    top: 180px;
    display: flex;
    justify-content: space-between;
    list-style: none;
  }
  .contacts__item {
    display: flex;
    align-items: center;
    gap: 8px;
    font-size: 13px;
    color: var(--text-dark);
  }
  .contacts__icon {
    width: 13px;
    height: 13px;
    fill: var(--orange);
    flex-shrink: 0;
  }
</style>
</head>
<body>
<main class="canvas">
  <section class="card card--front" aria-label="Card front">
    <div class="brand">
      <span class="brand__dot"></span>
      <span class="brand__name">Vantrel Systems</span>
    </div>
  </section>

  <section class="card card--back" aria-label="Card back">
    <div class="holder">
      <p class="holder__name">Your Name</p>
    </div>
    <div class="divider"></div>
    <p class="holder__title">JOB TITLE</p>

    <div class="brand">
      <span class="brand__dot"></span>
      <span class="brand__name">Vantrel Systems</span>
    </div>

    <ul class="contacts">
      <li class="contacts__item">
        <svg class="contacts__icon" viewBox="0 0 24 24" aria-hidden="true"><path d="M6.6 10.8a15.1 15.1 0 0 0 6.6 6.6l2.2-2.2a1 1 0 0 1 1-.25 11.4 11.4 0 0 0 3.6.57 1 1 0 0 1 1 1V20a1 1 0 0 1-1 1A17 17 0 0 1 3 4a1 1 0 0 1 1-1h3.5a1 1 0 0 1 1 1c0 1.25.2 2.45.57 3.6a1 1 0 0 1-.25 1z"/></svg>
        <span>000 000 0000</span>
      </li>
      <li class="contacts__item">
        <svg class="contacts__icon" viewBox="0 0 24 24" aria-hidden="true"><path d="M2 5h20v14H2z M2 5l10 8 10-8" fill="var(--orange)" stroke="#fff" stroke-width="1.5"/></svg>
        <span>youremail@xyz.com</span>
      </li>
      <li class="contacts__item">
        <svg class="contacts__icon" viewBox="0 0 24 24" aria-hidden="true"><circle cx="12" cy="12" r="10"/><path d="M2 12h20M12 2c3 3 3 17 0 20M12 2c-3 3-3 17 0 20" stroke="#fff" stroke-width="1.3" fill="none"/></svg>
        <span>www.yourwebsite.com</span>
      </li>
    </ul>
  </section>
</main>
</body>
</html>
```